Wedding Startup Full Website Design

We've just completed our online platform and need to create a website that represents our brand and vision, and clearly communicates our features and value proposition to potential users. There are a minimum of 4 pages that need to be designed. One geared toward wedding professionals (venues/vendors/coordinators), another toward engaged couples, one showcasing features, and an 'About Us' page.

The designer will creative freedom to create a unique UI/UX as long as it represents our brand and is relevant to our target audience/market. The ideal candidate will be able to assume the mindset of someone working in the wedding industry and/or an engaged couple. Ability to create illustrations is a plus.

Copy will be provided as needed. We will reimburse for stock images (pending approval before purchasing), but sourcing the stock images will be the responsibility of the designer.

Our current website: https://www.trelmora.com
Updates

Our project has now been guaranteed! We look forward to finding the perfect design for our site pages!

Still waiting for a design that stands out from the rest and aligns with the creative brief.

Target Market(s)

Wedding Professionals and Engaged Couples

Industry/Entity Type

Wedding

Number of Pages Required

4 page

Font styles to use
Sans Serif

Colors
ffffff
fbd4d5
f59195
33a6d7
cadf82
86cfc6

Requirements
Must have
• Common sense stuff like having a unified brand that accurately represents our platform, speaks to our target market, and clearly articulates our vision
Nice to have
• Illustrations
Should not have
• Overly cheesy or childish. We want to be professional but still embrace the wedding culture.

```html
<!DOCTYPE html>
<html lang="en">
<head>
<meta charset="utf-8">
<title>Trelmora — Smarter Wed Planning</title>
<link href="https://fonts.googleapis.com/css2?family=Lato:wght@300;400;700&display=swap" rel="stylesheet">
<style>
:root{
  --white:#ffffff;
  --blush:#fbd4d5;
  --coral:#f07f83;
  --blue:#33a6d7;
  --sky:#5ea9e6;
  --ink:#3b3b3b;
  --muted:#6d6d6d;
  --line:#dcdcdc;
  --mist:#f3f6f9;
}
*{margin:0;padding:0;box-sizing:border-box}
html,body{width:1200px;height:2975px;overflow:hidden}
body{font-family:'Lato',sans-serif;color:var(--ink);background:var(--white);position:relative}
.abs{position:absolute}
.brand{font-family:'Lato',sans-serif;font-weight:300;color:var(--sky);font-size:34px;letter-spacing:.5px}
.btn{position:absolute;background:var(--coral);color:var(--white);font-size:12px;font-weight:700;letter-spacing:.8px;display:flex;align-items:center;justify-content:center;text-transform:uppercase}
.header{position:absolute;left:0;top:0;width:1200px;height:76px;border-bottom:1px solid #e8ecf0;background:var(--white)}
.nav a{position:absolute;top:30px;font-size:14px;color:var(--muted);text-decoration:none}
.hero{position:absolute;left:0;top:76px;width:1200px;height:560px;background:linear-gradient(180deg,var(--mist),#ffffff)}
.photo{position:absolute}
.hero-photo{left:90px;top:96px;width:470px;height:500px;border-radius:46% 40% 44% 38%/38% 42% 48% 46%;background:radial-gradient(ellipse at 45% 45%,#9a8a7c 0%,#b8b1a8 45%,rgba(220,225,230,.4) 75%,rgba(255,255,255,0) 100%)}
.hero-title{left:578px;top:192px;font-size:50px;font-weight:300;color:var(--sky);opacity:.85}
.hero-sub{left:686px;top:270px;font-size:17px;color:var(--muted)}
.petal{position:absolute;border-radius:60% 40% 60% 40%;background:var(--blush);opacity:.85}
.h2{position:absolute;font-size:38px;font-weight:300;color:var(--sky)}
.step{position:absolute;left:188px;width:300px}
.step h3{font-size:15px;font-weight:400;margin-bottom:6px}
.step p{font-size:12px;line-height:18px;color:var(--muted)}
.step.faded h3,.step.faded p{color:#a8a8a8}
.step a{color:var(--coral)}
.dot{position:absolute;left:162px;width:10px;height:10px;border-radius:50%}
.app{position:absolute;left:538px;top:658px;width:508px;height:330px;border:1px solid #dfe4ea;background:var(--white);overflow:hidden;font-size:10px;color:#666}
.app .bar{height:22px;background:#eef0f3;border-bottom:1px solid #dde1e6}
.app .top{height:22px;background:#7fb4e8}
.app .side{position:absolute;left:0;top:44px;width:72px;bottom:0;border-right:1px solid #eceff2}
.app .row{position:absolute;height:7px;background:#c9ccd0}
.card{position:absolute;top:1080px;width:278px;height:250px;border:1px solid var(--line);text-align:center;padding:150px 22px 0}
.card p{font-size:12px;line-height:19px;color:var(--muted)}
.card b{color:var(--ink)}
.card svg{position:absolute;left:117px;top:40px}
.why{position:absolute;left:162px;width:378px;border-bottom:1px solid var(--line);height:96px}
.why svg{position:absolute;left:0;top:4px}
.why h3{position:absolute;left:52px;top:2px;font-size:15px;font-weight:400}
.why p{position:absolute;left:52px;top:28px;font-size:12px;line-height:19px;color:var(--muted)}
.grid{position:absolute;left:0;top:2290px;width:1200px;height:470px;display:grid;grid-template-columns:repeat(4,1fr);grid-template-rows:repeat(2,1fr);gap:4px}
.footer a{position:absolute;top:2897px;font-size:13px;color:var(--muted);text-decoration:none}
</style>
</head>
<body>

<header class="header">
  <div class="abs brand" style="left:160px;top:12px"><span style="display:inline-block;width:14px;height:14px;border:2px solid var(--coral);margin-right:6px;vertical-align:middle"></span>Trelmora</div>
  <nav class="nav">
    <a style="left:558px">About Us</a>
    <a style="left:662px">Features</a>
    <a style="left:763px">For Couples</a>
  </nav>
  <div class="btn" style="left:900px;top:20px;width:146px;height:36px">Acess Demo</div>
</header>

<section class="hero">
  <div class="photo hero-photo" style="top:20px" role="img" aria-label="Bride and groom embracing on a terrace, brushed edge"></div>
  <div class="abs hero-title" style="top:116px">Welcome to Trelmora</div>
  <div class="abs hero-sub" style="top:194px">Smarter Wed Planning™</div>
  <div class="btn" style="left:718px;top:244px;width:144px;height:36px">Get Started</div>
</section>

<div class="petal" role="img" aria-label="Rose petal" style="left:0;top:520px;width:95px;height:70px"></div>
<div class="petal" role="img" aria-label="Rose petal" style="left:20px;top:330px;width:22px;height:70px"></div>
<div class="petal" role="img" aria-label="Rose petal" style="left:1025px;top:205px;width:45px;height:55px"></div>
<div class="petal" role="img" aria-label="Rose petal" style="left:1125px;top:335px;width:75px;height:110px"></div>
<div class="petal" role="img" aria-label="Green petal" style="left:1005px;top:400px;width:85px;height:110px;background:#d9ebc3"></div>
<div class="petal" role="img" aria-label="Rose petal" style="left:1140px;top:128px;width:26px;height:16px"></div>

<div class="h2" style="left:158px;top:644px">How To Get Started</div>
<span class="dot" style="top:740px;background:var(--coral)"></span>
<div class="step" style="top:733px"><h3>Sign Up</h3><p>Create a free account on Trelmora to access popular collaboration tools. <a>Get Started</a></p></div>
<span class="dot" style="top:830px;background:var(--sky)"></span>
<div class="step faded" style="top:823px"><h3>Collaborate</h3><p>Add clients within the application to better organize and manage event details.</p></div>
<span class="dot" style="top:918px;background:var(--sky)"></span>
<div class="step faded" style="top:911px"><h3>Connect</h3><p>Linking your bank account within Trelmora to allow for seamless payments and monitoring.</p></div>

<div class="app">
  <div class="bar"></div><div class="top"></div>
  <div class="side"></div>
  <div class="abs" style="left:94px;top:54px;font-size:12px;color:#555">Maren Holt</div>
  <div class="abs" style="left:434px;top:52px;width:50px;height:14px;background:#7fb4e8;color:#fff;font-size:9px;text-align:center;line-height:14px">Print</div>
  <div class="abs" style="left:94px;top:78px">Event Date</div><div class="abs" style="left:250px;top:78px">Phone</div><div class="abs" style="left:380px;top:78px">Email</div>
  <div class="abs" style="left:88px;top:110px;font-size:12px;color:#555">Ceremony Guidelines</div>
  <div class="row" style="left:88px;top:130px;width:380px"></div>
  <div class="row" style="left:88px;top:144px;width:380px"></div>
  <div class="row" style="left:88px;top:158px;width:240px"></div>
  <div class="abs" style="left:88px;top:180px;font-size:8px">Brief description on how you are planning on having the ceremony site decorated</div>
  <div class="abs" style="left:88px;top:222px;font-size:8px">What is your wedding theme and color scheme?</div>
  <div class="abs" style="left:88px;top:264px;font-size:8px">Who is the primary contact the day of the wedding, and what is their email/phone number?</div>
  <div class="row" style="left:88px;top:290px;width:110px"></div><div class="row" style="left:210px;top:290px;width:60px"></div>
  <div class="abs" style="left:88px;top:308px;font-size:8px">List of everyone assisting with decorating.</div>
</div>

<div class="card" style="left:162px">
  <svg width="44" height="44" viewBox="0 0 44 44" fill="none" stroke="var(--sky)" stroke-width="2"><path d="M6 8h22a4 4 0 0 1 4 4v12a4 4 0 0 1-4 4H14l-8 6v-6a4 4 0 0 1-4-4V12a4 4 0 0 1 4-4z"/><path d="M32 16h6a4 4 0 0 1 4 4v10a4 4 0 0 1-4 4v5l-7-5h-9"/><path d="M10 16h14M10 21h10"/></svg>
  <p><b>Realtime Collaboration.</b> There are often disconnects in the communication channel. At the core of Trelmora we ensure everyone is updated in real time with event information.</p>
</div>
<div class="card" style="left:462px">
  <svg width="44" height="44" viewBox="0 0 44 44" fill="none" stroke="var(--sky)" stroke-width="2"><path d="M12 34H10a8 8 0 0 1 0-16 12 12 0 0 1 23-3 9 9 0 0 1 1 19h-2"/><path d="M22 36V20M16 26l6-6 6 6"/></svg>
  <p><b>Cloud Storage.</b> No longer do you have to remember where every piece of information is saved. With Trelmora all your information is available in one central location.</p>
</div>
<div class="card" style="left:762px">
  <svg width="44" height="44" viewBox="0 0 44 44" fill="none" stroke="var(--sky)" stroke-width="2"><path d="M22 6c-7 0-11 5-11 12v8l-4 6h30l-4-6v-8c0-7-4-12-11-12z" transform="rotate(20 22 22)"/><path d="M18 38a5 5 0 0 0 8 0"/></svg>
  <p><b>Notifications &amp; Deadlines.</b> Every detail is important and matters. Trelmora helps make sure that all the information for an event are inputted and updated in a timely manner.</p>
</div>

<div class="h2" style="left:158px;top:1410px">Why Trelmora</div>
<div class="photo" style="left:560px;top:1410px;width:640px;height:580px;border-radius:48% 42% 46% 40%/44% 40% 48% 44%;background:radial-gradient(ellipse at 55% 50%,#8f8070 0%,#b7b0a0 40%,rgba(205,215,200,.5) 70%,rgba(255,255,255,0) 100%)" role="img" aria-label="Couple kissing outdoors among greenery, brushed edge"></div>
<div class="petal" role="img" aria-label="Rose petal" style="left:1025px;top:1420px;width:55px;height:60px"></div>
<div class="petal" role="img" aria-label="Rose petal" style="left:20px;top:1550px;width:22px;height:70px"></div>
<div class="petal" role="img" aria-label="Rose petal" style="left:0;top:1740px;width:95px;height:80px"></div>

<div class="why" style="top:1490px">
  <svg width="34" height="34" viewBox="0 0 34 34" fill="none" stroke="var(--sky)" stroke-width="2"><circle cx="17" cy="17" r="14"/><path d="M17 9v8l6 4"/></svg>
  <h3>Saves Everyone Time</h3><p>Trelmora streamlines certain processes allowing you to spend more time on the things your want to or just relax!</p>
</div>
<div class="why" style="top:1592px">
  <svg width="34" height="34" viewBox="0 0 34 34" fill="none" stroke="var(--sky)" stroke-width="2"><path d="M4 5h26v18H14l-7 6v-6H4z"/><path d="M9 11h16M9 16h10"/></svg>
  <h3>Better Client Reviews</h3><p>With Trelmora you can offer your clients an experience they will rave about, leading to better reviews and more clients.</p>
</div>
<div class="why" style="top:1694px">
  <svg width="34" height="34" viewBox="0 0 34 34" fill="none" stroke="var(--sky)" stroke-width="2"><rect x="2" y="5" width="24" height="17"/><path d="M8 27h12"/><rect x="24" y="12" width="8" height="15"/></svg>
  <h3>Accessible on Any Device</h3><p>Flexibility is key, which is why Trelmora's platform was built to be accessed on your phone, tablet or desktop.</p>
</div>
<div class="why" style="top:1796px">
  <svg width="34" height="34" viewBox="0 0 34 34" fill="none" stroke="var(--sky)" stroke-width="2"><path d="M7 3h14l7 7v21H7z"/><path d="M12 14h11M12 19h11M12 24h8"/></svg>
  <h3>Simplified Organization</h3><p>Trelmora was built with organization in mind. All event details are in one place making executing an event easier.</p>
</div>
<div class="why" style="top:1898px">
  <svg width="34" height="34" viewBox="0 0 34 34" fill="none" stroke="var(--sky)" stroke-width="2"><rect x="3" y="8" width="28" height="19" rx="2"/><path d="M3 14h28M8 22h8"/></svg>
  <h3>Lower Transaction Fees</h3><p>We offer the lowest online processing fees (2.65%) in the wedding industry, meaning you keep more of your money.</p>
</div>

<div class="h2" style="left:158px;top:2074px">Get Started Today</div>
<p class="abs" style="left:162px;top:2132px;width:460px;font-size:12px;line-height:19px;color:var(--muted)">We recently launched a demo version of Trelmora to allow users to see and interact with our platform. Create a free account and see how Trelmora is changing the wedding planning process!</p>
<div class="btn" style="left:162px;top:2212px;width:144px;height:36px">Get Started</div>
<div class="photo" style="left:840px;top:2075px;width:150px;height:195px;border-radius:40%;background:radial-gradient(circle,#f4f1ec 0%,#e4e2dc 55%,rgba(255,255,255,0) 75%)" role="img" aria-label="Lace heart ornament with white roses"></div>

<div class="grid">
  <div role="img" aria-label="Couple dancing at reception" style="background:linear-gradient(135deg,#6b6a5e,#b9b3a6)"></div>
  <div role="img" aria-label="Couple cutting the wedding cake" style="background:linear-gradient(135deg,#7d776c,#d6d2c8)"></div>
  <div role="img" aria-label="Reception table setting" style="background:linear-gradient(135deg,#8a6a4c,#d9c3a0)"></div>
  <div role="img" aria-label="Mr and Mrs chair signs" style="background:linear-gradient(135deg,#7a5d45,#c9b49a)"></div>
  <div role="img" aria-label="Wedding party outdoors" style="background:linear-gradient(135deg,#5f6a55,#c7c4bb)"></div>
  <div role="img" aria-label="Wedding rings on wood" style="background:linear-gradient(135deg,#8c7a66,#e6ddd2)"></div>
  <div role="img" aria-label="Couple walking down the aisle" style="background:linear-gradient(135deg,#56604a,#a9ae96)"></div>
  <div role="img" aria-label="Bride having makeup applied" style="background:linear-gradient(135deg,#6e5a4e,#e1c9b5)"></div>
</div>

<footer class="footer">
  <div class="abs brand" style="left:530px;top:2818px"><span style="display:inline-block;width:14px;height:14px;border:2px solid var(--coral);margin-right:6px;vertical-align:middle"></span>Trelmora</div>
  <a style="left:474px">About Us</a>
  <a style="left:583px">Features</a>
  <a style="left:682px">For Couples</a>
  <div class="abs" style="left:0;top:2928px;width:1200px;text-align:center;font-size:13px;color:var(--muted)">© 2018 trelmora. All Rights Reserved.</div>
</footer>

</body>
</html>
```